Need an introduce flyer for dental clinic

We are a dental clinic, need a design of flyer for introduce about service
Size: A4
Content: Please visit our website https://pinebrookdentalhub.example/procedures
In this page, please choose 3 content for explain:
- Teeth Whitenning
- Implant
- Replace
We need a footer include contact information and a QR code direct to our page.

Target Market(s)

Age from 27-55

Industry/Entity Type

Medical

Font styles to use
Sans Serif

Colors
33a6d7
85cae6

Requirements
Must have
• Picture for dental clinic
Nice to have
• Place holder
Should not have
• Too much colors

```html
<!DOCTYPE html>
<html lang="en">
<head>
<meta charset="utf-8">
<title>Pinebrook Dental – Flyer</title>
<link rel="stylesheet" href="https://fonts.googleapis.com/css2?family=Roboto:wght@400;500;700&display=swap">
<style>
  :root {
    --backdrop: #e9e7e5;
    --navy: #123a7a;
    --deep-blue: #1d4f9c;
    --teal: #3bb0a8;
    --sky: #33a6d7;
    --pale-sky: #85cae6;
    --white: #ffffff;
    --ink: #1c2a4a;
    --logo-green: #2f8a3a;
  }
  * { box-sizing: border-box; margin: 0; padding: 0; }
  html, body {
    width: 1200px; height: 688px; overflow: hidden;
    background: var(--backdrop);
    font-family: "Roboto", Arial, sans-serif;
  }
  .flyer {
    position: absolute; left: 374px; top: 24px;
    width: 452px; height: 640px;
    background: var(--white);
    overflow: hidden;
    box-shadow: 0 2px 8px rgba(0,0,0,0.12);
  }
  .clinic-photo {
    position: absolute; left: 0; top: 0; width: 452px; height: 436px;
    background:
      radial-gradient(ellipse at 70% 40%, #d9eef3 0%, rgba(217,238,243,0) 55%),
      linear-gradient(160deg, #eef3f6 0%, #bcd3e4 45%, #8cc7e0 75%, #6fc6cf 100%);
  }
  .services-column {
    position: absolute; left: 0; top: 0; width: 236px; height: 436px;
    padding: 46px 16px 0 18px;
    background: linear-gradient(170deg, rgba(18,58,122,0.94) 0%, rgba(37,92,160,0.88) 45%, rgba(59,176,168,0.82) 100%);
    color: var(--white);
  }
  .service { margin-bottom: 20px; }
  .service-title {
    display: flex; align-items: center; gap: 8px;
    font-size: 13px; font-weight: 500; letter-spacing: 0.6px;
    text-transform: uppercase; margin-bottom: 6px;
  }
  .service-icon { width: 18px; height: 18px; flex: none; }
  .service-text { font-size: 6.5px; line-height: 1.5; opacity: 0.92; }
  .info-band {
    position: absolute; left: 0; top: 436px; width: 452px; height: 204px;
    background: linear-gradient(100deg, var(--navy) 0%, var(--deep-blue) 45%, var(--sky) 100%);
  }
  .accent-stripe {
    position: absolute; left: 236px; top: 372px; width: 216px; height: 6px;
    background: linear-gradient(90deg, var(--navy), var(--deep-blue));
  }
  .edge-band {
    position: absolute; left: 440px; top: 378px; width: 12px; height: 58px;
    background: linear-gradient(180deg, var(--deep-blue), var(--sky));
  }
  .info-content {
    position: absolute; left: 18px; top: 448px; width: 206px; color: var(--white);
  }
  .clinic-name { font-size: 23px; font-weight: 700; line-height: 1; white-space: nowrap; }
  .clinic-location { font-size: 14px; font-weight: 400; margin-top: 3px; }
  .divider { height: 1px; background: rgba(255,255,255,0.6); margin: 10px 0 12px; }
  .tagline { font-size: 11px; font-weight: 500; margin-bottom: 5px; }
  .intro { font-size: 6.5px; line-height: 1.5; margin-bottom: 16px; }
  .contact-row { display: flex; align-items: center; gap: 8px; font-size: 8px; margin-bottom: 8px; }
  .contact-row svg { width: 12px; height: 12px; flex: none; }
  .logo-panel {
    position: absolute; left: 236px; top: 378px; width: 204px; height: 248px;
    background: var(--white);
    display: flex; flex-direction: column; align-items: center; justify-content: center;
    text-align: center;
  }
  .brand-mark { display: flex; align-items: center; gap: 7px; margin-bottom: 26px; }
  .brand-dot { width: 14px; height: 14px; border-radius: 50%; background: var(--logo-green); }
  .brand-name { font-size: 20px; font-weight: 700; color: var(--logo-green); }
  .placeholder-note { font-size: 7px; line-height: 1.4; color: var(--ink); width: 150px; }
</style>
</head>
<body>
  <div class="flyer">
    <div class="clinic-photo" role="img" aria-label="Photo of a smiling patient receiving a dental check-up from a gloved dentist in a bright clinic"></div>

    <section class="services-column">
      <div class="service">
        <h2 class="service-title">
          <svg class="service-icon" viewBox="0 0 18 18"><circle cx="9" cy="9" r="9" fill="#fff"/><path d="M5.5 6c0-1.5 1.5-2 3.5-1.2C11 4 12.5 4.5 12.5 6c0 2-1 3-1.3 6-.2 1-1 1-1.2 0L9 9.5 8 12c-.2 1-1 1-1.2 0C6.5 9 5.5 8 5.5 6z" fill="#123a7a"/></svg>
          Teeth Whitening
        </h2>
        <p class="service-text">Our clinic offers three whitening systems to brighten your smile. Treatments are gentle, quick and tailored to your enamel, with results you can see after one visit and care tips to keep them.</p>
      </div>
      <div class="service">
        <h2 class="service-title">
          <svg class="service-icon" viewBox="0 0 18 18"><circle cx="9" cy="9" r="9" fill="#fff"/><path d="M5.5 6c0-1.5 1.5-2 3.5-1.2C11 4 12.5 4.5 12.5 6c0 2-1 3-1.3 6-.2 1-1 1-1.2 0L9 9.5 8 12c-.2 1-1 1-1.2 0C6.5 9 5.5 8 5.5 6z" fill="#123a7a"/></svg>
          Implants
        </h2>
        <p class="service-text">A missing tooth can lead to bone loss over time. Implants replace the root and crown, restoring strength and comfort. Our team plans each step with care so healing is smooth and the result looks natural.</p>
      </div>
      <div class="service">
        <h2 class="service-title">
          <svg class="service-icon" viewBox="0 0 18 18"><circle cx="9" cy="9" r="9" fill="#fff"/><path d="M5.5 6c0-1.5 1.5-2 3.5-1.2C11 4 12.5 4.5 12.5 6c0 2-1 3-1.3 6-.2 1-1 1-1.2 0L9 9.5 8 12c-.2 1-1 1-1.2 0C6.5 9 5.5 8 5.5 6z" fill="#123a7a"/></svg>
          Replace
        </h2>
        <p class="service-text">Daily life is hard when a tooth is lost or damaged. We offer bridges, crowns and dentures that fit well and feel like your own, made with modern tools and years of skill.</p>
      </div>
    </section>

    <div class="info-band"></div>
    <div class="accent-stripe"></div>
    <div class="edge-band"></div>

    <div class="info-content">
      <h1 class="clinic-name">Pinebrook Dental</h1>
      <p class="clinic-location">Korea</p>
      <div class="divider"></div>
      <p class="tagline">Voted Best Dentist in Asia</p>
      <p class="intro">Pinebrook Dental is the number one dental office in Korea. Helmed by Dr. Han, you are guaranteed a beautiful smile and a wonderful experience.</p>
      <p class="contact-row">
        <svg viewBox="0 0 12 12"><circle cx="6" cy="6" r="5.5" fill="none" stroke="#fff" stroke-width="0.8"/><path d="M4 3.2l1 1.4-.6.7c.4.8 1 1.4 1.8 1.8l.7-.6 1.4 1-.6 1C6 8.3 3.7 6 3.2 4.3z" fill="#fff"/></svg>
        +82 10.5550.0142
      </p>
      <p class="contact-row">
        <svg viewBox="0 0 12 12"><rect x="1" y="2.5" width="10" height="7" fill="none" stroke="#fff" stroke-width="0.8"/><path d="M1 2.5l5 4 5-4" fill="none" stroke="#fff" stroke-width="0.8"/></svg>
        pinebrookclinic@example.com
      </p>
    </div>

    <aside class="logo-panel">
      <div class="brand-mark">
        <span class="brand-dot"></span>
        <span class="brand-name">Pinebrook</span>
      </div>
      <p class="placeholder-note">Include contact information and a QR code direct to your page, here.</p>
    </aside>
  </div>
</body>
</html>
```